Service Plan Sales Flyer

The Watchpost Depot (www.kelvamart.com) is a commercial security integrator that installs security cameras, access control, intrusion, two-way radios and perimeter security. We require a one page flyer for our service plan for new and existing customers. The price of the service plan is $299/yr and includes the following;
1. Discounted service rate of $118/hr
2. Free remote support ($85/hr without a plan)
3. Free remote training
4. Priority support

Please review our brochure attached and create a one page sales flyer with the end goal of having the client sign up for our annual service plan . The plan will automatically renew every year. Email sales@kelvamart.com.

Target Market(s)

commercial industrial clients - no residential

Industry/Entity Type

review our website at www.kelvamart.com

Colors
0054AA
0677BA
7BADD7
CADEEF
E8F1F8
EE7325
F08F49
F5BC92
FAE3D3
FDF4ED

Requirements
Must have
• call to action
Should not have
• too many colors

```html
<!DOCTYPE html>
<html lang="en">
<head>
<meta charset="utf-8">
<title>The Watchpost Depot – Annual Service Plan Flyer</title>
<link href="https://fonts.googleapis.com/css2?family=Oswald:wght@600;700&family=Poppins:wght@400;500;600;700;800&display=swap" rel="stylesheet">
<style>
  :root{
    --navy:#0c2a5b;
    --navy-deep:#081d42;
    --red:#ee3a31;
    --white:#ffffff;
    --ink:#1c2233;
    --stage:#e4e7ea;
  }
  *{margin:0;padding:0;box-sizing:border-box}
  html,body{width:1200px;height:2400px;overflow:hidden;background:var(--stage)}
  body{position:relative;font-family:"Poppins",sans-serif}
  .flyer{
    position:absolute;left:0;top:351px;width:958px;height:1355px;
    transform:scale(1.25261);transform-origin:0 0;background:var(--white);overflow:hidden;
  }
  .abs{position:absolute}
  .header-shapes{position:absolute;left:0;top:0;width:958px;height:430px}
  .brand{left:55px;top:68px;display:flex;align-items:center;gap:14px}
  .brand-mark{width:34px;height:34px;background:var(--red)}
  .brand-name{font-weight:800;font-size:30px;color:var(--white);letter-spacing:.5px;text-transform:uppercase;line-height:1}
  .headline{left:53px;top:160px;line-height:1}
  .headline .lead{display:block;font-family:"Oswald",sans-serif;font-weight:700;font-size:66px;color:var(--red);letter-spacing:.5px}
  .headline .main{display:block;font-weight:800;font-size:55px;color:var(--white);line-height:56px}
  .tagline{left:52px;top:347px;font-weight:600;font-size:16.5px;letter-spacing:3.2px;color:var(--white)}
  .tagline .bar{color:var(--red);margin:0 6px}
  .camera-photo{left:560px;top:372px;width:330px;height:110px;border-radius:55px 20px 20px 55px;
    background:linear-gradient(100deg,#cfd3d8 0%,#f4f5f6 45%,#b9bdc2 100%)}
  .devices-photo{left:610px;top:500px;width:285px;height:200px;border-radius:12px;
    background:linear-gradient(160deg,#3a3f47 0%,#15181d 60%,#6b7078 100%)}
  .intro{left:53px;top:432px;font-weight:700;font-size:27px;line-height:33px;color:var(--red)}
  .service-band{left:0;top:595px;width:600px;height:115px;background:var(--red)}
  .service-band .divider{position:absolute;top:0;width:2px;height:115px;background:rgba(255,255,255,.35)}
  .service{position:absolute;top:-38px;width:140px;text-align:center}
  .service .icon{width:64px;height:64px;margin:0 auto;border-radius:50%;background:var(--navy);border:3px solid var(--white);display:flex;align-items:center;justify-content:center}
  .service .label{margin-top:6px;font-weight:600;font-size:16px;line-height:19px;color:var(--white)}
  .plan-title{left:48px;top:735px;font-weight:800;font-size:34px;line-height:33px;color:var(--navy)}
  .plan-price{left:318px;top:752px;font-weight:800;font-size:46px;color:var(--red);line-height:1}
  .plan-price small{font-size:22px;font-weight:700}
  .includes{left:48px;top:818px;width:452px;height:292px;border:1.6px dashed var(--red);border-radius:12px}
  .includes-title{left:75px;top:826px;font-weight:600;font-size:26px;color:var(--ink)}
  .benefit{position:absolute;left:70px;display:flex;align-items:center;gap:14px;font-size:18.5px;line-height:22px;color:var(--ink)}
  .benefit .dot{width:42px;height:42px;flex:none;border-radius:50%;background:var(--red);border:3px solid #f7c9c6;display:flex;align-items:center;justify-content:center}
  .cta{left:53px;top:1132px;font-weight:700;font-size:26px;line-height:30px}
  .cta .red{color:var(--red)}
  .cta .navy{color:var(--navy)}
  .contact{position:absolute;left:52px;display:flex;align-items:center;gap:20px;font-size:24px;color:var(--ink)}
  .contact .ci{width:24px;height:24px;flex:none;border-radius:50%;background:var(--navy);display:flex;align-items:center;justify-content:center}
  .contact .hl{color:var(--red);font-weight:600}
  .steps-panel{left:553px;top:710px;width:350px;height:645px;
    background:radial-gradient(ellipse at 50% 70%,#1d4f9a 0%,#0f3270 45%,var(--navy-deep) 100%)}
  .steps-head{left:553px;top:780px;width:350px;text-align:center;color:var(--white);font-weight:800}
  .steps-head .l1{font-size:30px;line-height:32px}
  .steps-head .l2{font-size:22px;line-height:26px;font-weight:700}
  .steps-pill{left:538px;top:855px;width:340px;height:56px;background:var(--red);border-radius:0 10px 10px 0;
    color:var(--white);font-weight:800;font-size:29px;line-height:52px;text-align:center;border:2px solid #ff6a62}
  .step{position:absolute;left:590px;display:flex;align-items:center;gap:16px;color:var(--white)}
  .step .num{font-family:"Oswald",sans-serif;font-weight:700;font-size:54px;color:var(--red);width:30px;line-height:1}
  .step .txt{font-weight:500;font-size:18.5px;line-height:22px;text-transform:uppercase}
  .step-rule{position:absolute;left:573px;width:278px;border-top:1.5px dashed rgba(238,58,49,.75)}
</style>
</head>
<body>
<main class="flyer">
  <svg class="header-shapes" viewBox="0 0 958 430" aria-hidden="true">
    <defs>
      <linearGradient id="photoTone" x1="0" y1="0" x2="1" y2="1">
        <stop offset="0" stop-color="#16181b"/>
        <stop offset=".45" stop-color="#5b5f64"/>
        <stop offset="1" stop-color="#1e2023"/>
      </linearGradient>
    </defs>
    <polygon points="0,0 520,0 448,402 0,402" fill="#0c2a5b"/>
    <polygon points="430,402 448,402 445,418 430,418" fill="#ee3a31"/>
    <polygon points="520,0 545,0 468,420 443,420" fill="#ee3a31"/>
    <polygon points="545,0 958,0 958,420 468,420" fill="url(#photoTone)"/>
  </svg>
  <div class="abs" role="img" aria-label="Photo of a security camera with a glowing padlock target overlay" style="left:560px;top:0;width:398px;height:420px"></div>

  <div class="abs brand">
    <span class="brand-mark"></span>
    <span class="brand-name">The Watchpost Depot</span>
  </div>

  <h1 class="abs headline">
    <span class="lead">COMMERCIAL</span>
    <span class="main">SECURITY</span>
    <span class="main">INTEGRATOR</span>
  </h1>
  <p class="abs tagline">KNOWLEDGEABLE<span class="bar">|</span>RELIABLE<span class="bar">|</span>EASY</p>

  <div class="abs camera-photo" role="img" aria-label="Photo of a white bullet security camera"></div>

  <p class="abs intro">The Watchpost Depot<br>is a commercial security<br>integrator that installs</p>

  <section class="abs service-band">
    <span class="divider" style="left:185px"></span>
    <span class="divider" style="left:325px"></span>
    <span class="divider" style="left:467px"></span>
    <div class="service" style="left:40px">
      <div class="icon"><svg width="30" height="30" viewBox="0 0 30 30" fill="none" stroke="#fff" stroke-width="2"><rect x="4" y="8" width="18" height="9" rx="2" transform="rotate(15 13 12)"/><path d="M9 19v7M5 26h8M20 15l6 2"/></svg></div>
      <div class="label">Serveillance<br>Cameras</div>
    </div>
    <div class="service" style="left:182px">
      <div class="icon"><svg width="30" height="30" viewBox="0 0 30 30" fill="none" stroke="#fff" stroke-width="2"><circle cx="19" cy="11" r="6"/><path d="M15 15 5 25M8 22l3 3M11 19l2 2"/></svg></div>
      <div class="label">Access<br>Control &amp;<br>Intercom</div>
    </div>
    <div class="service" style="left:323px">
      <div class="icon"><svg width="30" height="30" viewBox="0 0 30 30" fill="none" stroke="#fff" stroke-width="2"><path d="M15 3 25 7v7c0 7-5 11-10 13C10 25 5 21 5 14V7z"/><rect x="11" y="13" width="8" height="7"/><path d="M12.5 13v-2a2.5 2.5 0 0 1 5 0v2"/></svg></div>
      <div class="label">Permeter<br>Security</div>
    </div>
    <div class="service" style="left:464px">
      <div class="icon"><svg width="30" height="30" viewBox="0 0 30 30" fill="none" stroke="#fff" stroke-width="2"><rect x="4" y="8" width="14" height="17" rx="2"/><path d="M8 4v4M8 13h6M8 17h2M12 17h2"/><path d="M21 15l6 2v4c0 3-3 5-6 6-3-1-6-3-6-6v-4z"/></svg></div>
      <div class="label">Intrusion<br>Alarm</div>
    </div>
  </section>

  <h2 class="abs plan-title">ANNUAL<br>SERVICE PLAN</h2>
  <p class="abs plan-price">$299<small>/YR</small></p>
  <div class="abs includes"></div>
  <h3 class="abs includes-title">Includes the following:</h3>
  <p class="benefit" style="top:870px"><span class="dot"><svg width="18" height="18" viewBox="0 0 18 18" fill="none" stroke="#fff" stroke-width="2"><path d="M4 14 14 4"/><circle cx="5" cy="5" r="2"/><circle cx="13" cy="13" r="2"/></svg></span><span>Discounted service rate of <b>$118/hr</b></span></p>
  <p class="benefit" style="top:930px"><span class="dot"><svg width="18" height="18" viewBox="0 0 18 18" fill="none" stroke="#fff" stroke-width="2"><rect x="5" y="2" width="8" height="14" rx="2" transform="rotate(30 9 9)"/></svg></span><span>Free remote support<br><b>($85/hr without a plan)</b></span></p>
  <p class="benefit" style="top:997px"><span class="dot"><svg width="18" height="18" viewBox="0 0 18 18" fill="none" stroke="#fff" stroke-width="2"><path d="M9 2a5 5 0 0 1 3 9v2H6v-2a5 5 0 0 1 3-9zM6 16h6"/></svg></span><span><b>Free</b> remote training</span></p>
  <p class="benefit" style="top:1052px"><span class="dot"><svg width="18" height="18" viewBox="0 0 18 18" fill="none" stroke="#fff" stroke-width="2"><path d="M3 10a6 6 0 0 1 12 0M3 10v3h2v-3zM15 10v3h-2v-3z"/></svg></span><span>Priority support</span></p>

  <p class="abs cta"><span class="red">Contact us to request a</span><br><span class="navy">FREE quote and security plan.</span></p>
  <p class="contact" style="top:1200px"><span class="ci"><svg width="13" height="13" viewBox="0 0 14 14" fill="#fff"><path d="M3 1l2 3-1.3 1.3a8 8 0 0 0 5 5L10 9l3 2-1.5 2.5C6 13 1 8 .5 2.5z"/></svg></span><span>1-877-555-0147</span></p>
  <p class="contact" style="top:1238px"><span class="ci"><svg width="13" height="13" viewBox="0 0 14 14" fill="none" stroke="#fff" stroke-width="1.6"><rect x="1.5" y="3" width="11" height="8"/><path d="M1.5 3 7 8l5.5-5"/></svg></span><span>sales@kelvamart.com</span></p>
  <p class="contact" style="top:1276px"><span class="ci"><svg width="13" height="13" viewBox="0 0 14 14" fill="none" stroke="#fff" stroke-width="1.4"><circle cx="7" cy="7" r="5.5"/><path d="M1.5 7h11M7 1.5c-3 3.5-3 7.5 0 11M7 1.5c3 3.5 3 7.5 0 11"/></svg></span><span>www.<span class="hl">kelvamart</span>.com</span></p>

  <aside class="abs steps-panel"></aside>
  <div class="abs devices-photo" role="img" aria-label="Photo of a smartphone, tablet and dome camera showing an access control app"></div>
  <div class="abs steps-head"><p class="l1">SIGN UP FOR OUR</p><p class="l2">Annual subscription Plan</p></div>
  <p class="abs steps-pill">WITH 5 EASY STEPS</p>

  <div class="step" style="top:925px"><span class="num">1</span><span class="txt">Needs<br>Consultation</span></div>
  <span class="step-rule" style="top:995px"></span>
  <div class="step" style="top:1013px"><span class="num">2</span><span class="txt">Custom Quote</span></div>
  <span class="step-rule" style="top:1077px"></span>
  <div class="step" style="top:1094px"><span class="num">3</span><span class="txt">Installation</span></div>
  <span class="step-rule" style="top:1162px"></span>
  <div class="step" style="top:1170px"><span class="num">4</span><span class="txt">Ongoing Support</span></div>
  <span class="step-rule" style="top:1240px"></span>
  <div class="step" style="top:1250px"><span class="num">5</span><span class="txt">Improvements<br>&amp; Updates</span></div>
</main>
</body>
</html>
```